Quillmont Renovations Letterhead

Quillmont does not do actual renovation, but rather handles high end project management of renovation (primarily residential with an eye toward commercial and International) The renovation work could look very different between projects. This company works directly with the clients and manages the work of contractors, architects and interior designers (either subcontracted directly by Quillmont or hired by the client and entrusted to Quillmont to manage). Clients are high end in the economic scale and all materials should speak to that audience. Provoke a sense of change, openness and imagination, trust and integrity. The owner is female, but the audience will be heavily slanted male. It should not be a "feminine" or "masculine" looking . If anything, slant more on the masculine side.

Clean, simple, yet creative and artistically appealing. The logo should be clear and not competing with too many surrounding design elements.

There is a contest also on for business card. Please check that section if you would like to compete for both.

Get your creative juices going!

Target Market(s)

High end cients. Additional audience: professionals (architects, etc...) designers, contractors

Industry/Entity Type

Residential

Requirements
Must have
• Logo must be included in all materials

```html
<!DOCTYPE html>
<html lang="en">
<head>
<meta charset="utf-8">
<title>Quillmont Renovations Letterhead</title>
<link href="https://fonts.googleapis.com/css2?family=Questrial&family=Old+Standard+TT:wght@700&display=swap" rel="stylesheet">
<style>
  :root {
    --paper: #f2f2f2;
    --charcoal: #4d4d4d;
    --edge: #2b2b2b;
    --teal: #1fab9f;
    --white: #ffffff;
  }
  html, body {
    margin: 0;
    padding: 0;
    width: 927px;
    height: 1200px;
    overflow: hidden;
    background: var(--paper);
  }
  .letterhead {
    position: relative;
    width: 927px;
    height: 1200px;
    background: var(--paper);
    box-sizing: border-box;
    border: 2px solid var(--edge);
    overflow: hidden;
  }
  .roofline {
    position: absolute;
    left: 0;
    top: 0;
    width: 927px;
    height: 240px;
  }
  .roofline polygon { fill: var(--charcoal); }
  .brand-name {
    position: absolute;
    left: 538px;
    top: 206px;
    margin: 0;
    font-family: "Questrial", "Century Gothic", sans-serif;
    font-weight: 400;
    font-size: 25px;
    letter-spacing: 0.5px;
    color: var(--charcoal);
    white-space: nowrap;
  }
  .footer-band {
    position: absolute;
    left: 0;
    bottom: 0;
    width: 927px;
    height: 102px;
  }
  .footer-band .band-teal { fill: var(--teal); }
  .footer-band .band-charcoal { fill: var(--charcoal); }
  .footer-band .divider { stroke: var(--white); stroke-width: 1.5; }
  .footer-text {
    position: absolute;
    margin: 0;
    font-family: "Old Standard TT", "Century Schoolbook", serif;
    font-weight: 700;
    font-size: 15px;
    line-height: 24px;
    color: var(--white);
    white-space: nowrap;
  }
  .legal { left: 38px; top: 1125px; }
  .address { left: 353px; top: 1125px; }
  .phones { left: 573px; top: 1125px; }
  .online { left: 753px; top: 1125px; }
</style>
</head>
<body>
  <main class="letterhead">
    <svg class="roofline" viewBox="0 0 927 240" aria-hidden="true">
      <polygon points="0,232 527,4 730,91 688,91 527,28 122,205 202,205 202,232"/>
    </svg>

    <p class="brand-name">QUILLMONT RENOVATIONS</p>

    <svg class="footer-band" viewBox="0 0 927 102" aria-hidden="true">
      <rect class="band-teal" x="0" y="0" width="927" height="102"/>
      <polygon class="band-charcoal" points="0,0 371,0 227,102 0,102"/>
      <line class="divider" x1="562" y1="12" x2="562" y2="87"/>
      <line class="divider" x1="744" y1="12" x2="744" y2="87"/>
    </svg>

    <p class="footer-text legal">Legal information</p>
    <p class="footer-text address">Adress :</p>
    <p class="footer-text phones">Tel&nbsp; : 00 00 00 00 00<br>Fax : 00 00 00 00 00</p>
    <p class="footer-text online">www.website.com<br>email@email.com</p>
  </main>
</body>
</html>
```